Technology Podcast Cover Art Design

Title: The Wayfinders
Subtitle: A podcast about the future of all of us

site:

https://wayfindcast.example (ignore the colors/theme of site, we can change this as needed to suit new cover)

here is the description to give idea what podcast is about:
The Wayfinders is like a longform KIVO Lecture, a podcast about the future of all of us where look at the technologies, trends and societal norms shaping our collective future. Here the world’s disruptive top minds share their passion projects and how advances in genomics, robotics, space travel, IoT, artificial intelligence and other exponential tech is converging to create the future of tomorrow.

Two minds are better than one, and the purpose of this podcast is to create a worldwide “neural network” of connected human creators to tackle society’s big problems like climate change, aging, inequality, disease… you name it.

The #1 problem plaguing humanity is short term thinking. If in-depth, unscripted conversations with the scientists, startups and thought leaders daring to dream bigger is your cup of tea, you have come to the right place.

--

Target audience:
similar to Kivo.example, innovative creatives, scientists, startups, politicians... mainly smart people interested in future

Avoid:
DO NOT have a picture of a microphone in the cover art

What needs to be written:
the only thing that HAS to be written is: The Wayfinders

you can also add the subtitle (but you don't have to): A podcast about the future of all of us

you can also add host info (but you don't have to): with Lena Horvik

--

in terms of colors, we would prefer bright colors, probably blue or orange but if you make an awesome cover we can use that instead

```html
<!DOCTYPE html>
<html lang="en">
<head>
<meta charset="utf-8">
<title>The Wayfinders — Podcast Cover</title>
<link rel="stylesheet" href="https://fonts.googleapis.com/css2?family=Bebas+Neue&display=swap">
<style>
  :root {
    --ink: #000000;
    --sky: #00aeef;
    --steel: #959595;
    --paper: #ffffff;
  }
  html, body {
    margin: 0;
    padding: 0;
    width: 1200px;
    height: 1200px;
    overflow: hidden;
    background: var(--ink);
  }
  .cover {
    display: block;
    width: 1200px;
    height: 1200px;
    background: var(--ink);
  }
  .rule { stroke: var(--sky); stroke-width: 2; }
  .kicker {
    font-family: "Bebas Neue", sans-serif;
    font-size: 31px;
    letter-spacing: 6px;
    fill: var(--paper);
  }
  .title {
    font-family: "Bebas Neue", sans-serif;
    font-size: 284px;
    fill: var(--sky);
  }
  .tagline {
    font-family: "Bebas Neue", sans-serif;
    font-size: 39px;
    fill: var(--paper);
  }
</style>
</head>
<body>
<svg class="cover" viewBox="0 0 1200 1200" xmlns="http://www.w3.org/2000/svg" aria-labelledby="cover-title">
  <title id="cover-title">The Wayfinders — a podcast about the future of all of us</title>
  <defs>
    <linearGradient id="signal-tone" x1="0" y1="0" x2="1" y2="0">
      <stop offset="0" stop-color="var(--sky)" stop-opacity="0.55"/>
      <stop offset="0.5" stop-color="var(--steel)" stop-opacity="0.55"/>
      <stop offset="1" stop-color="var(--sky)" stop-opacity="0.55"/>
    </linearGradient>
  </defs>

  <g class="masthead">
    <line class="rule" x1="63" y1="434" x2="549" y2="434"/>
    <line class="rule" x1="641" y1="434" x2="1125" y2="434"/>
    <text class="kicker" x="598" y="446" text-anchor="middle">THE</text>
  </g>

  <text class="title" x="63" y="670" textLength="1077" lengthAdjust="spacingAndGlyphs">WAYFINDERS</text>

  <rect class="signal-band" x="226" y="939" width="700" height="43"
        fill="url(#signal-tone)" role="img" aria-label="Decorative band of horizontal signal lines in blue and grey"/>

  <text class="tagline" x="341" y="1025" textLength="513" lengthAdjust="spacingAndGlyphs">A PODCAST ABOUT THE FUTURE OF ALL OF US</text>

  <rect class="signal-band" x="220" y="1037" width="776" height="47"
        fill="url(#signal-tone)" role="img" aria-label="Decorative band of horizontal signal lines in blue and grey"/>
</svg>
</body>
</html>
```